Free Printer Promotion

Hi i need a banner AD for my website.

The promotion is: free printer, for a monthly cost you get all the supplies and service included. Its a subscription service for printing. There is 5 plans available.
Prices vary upon printers, most expensive plan is $69.94 a month for a 1 year term and the most affordable plan is $9.95 a month for 3 year term

1 Monochrome laser (print only printer, black and white printing)
2 Multifunction Monochrome laser (print scan copy fax printer, black and white printing)

• Monochrome Printers are given 1000 prints per month
• Toner included
• Service included
• Printer included

3 Color laser (print only printer, color printing)
4 Multifunction Color laser (print scan copy fax, color printing)
Color printers are given 500 monochrome prints and 500 color prints per month
• Toner included
• Service included
• Printer included

5 Inkjet color printer (print copy scan fax, color printing)
• Inkjet Printers are given 1000 prints per month.
• Ink included
• Service included
• Printer included

Target Market(s)

students, home office workers, corporate business and government

Font styles to use
Serif
Sans Serif

Requirements
Must have
• i want it to be enticing, no long sentences. the customer will click on the banner and it will bring them to another page with the information.

Keep it short and sweet.

```html
<!DOCTYPE html>
<html lang="en">
<head>
<meta charset="utf-8">
<title>Free Printer – Subscription Printing Plans</title>
<link href="https://fonts.googleapis.com/css2?family=Oswald:wght@600;700&family=Roboto+Condensed:wght@400&family=Roboto:wght@400;500;700&display=swap" rel="stylesheet">
<style>
  :root{
    --brand-blue:#036a8f;
    --title-blue:#0f6f97;
    --charcoal:#3a3a3c;
    --navy:#0c1a44;
    --ink:#1b2a3a;
    --pale-band:#e3eef1;
    --footer-grey:#e6e6e6;
    --white:#ffffff;
  }
  *{margin:0;padding:0;box-sizing:border-box}
  html,body{width:1200px;height:2400px;overflow:hidden;background:var(--white)}
  .banner{position:relative;width:1200px;height:2400px;font-family:"Roboto",Arial,sans-serif;color:var(--ink);background:var(--white)}
  .hero{position:absolute;left:0;top:0;width:1200px;height:494px;
    background:linear-gradient(90deg,#f4f6f8 0%,#eef2f6 50%,#f6f8fb 100%)}
  .hero-photo{position:absolute;left:0;top:0;width:560px;height:494px;
    background:linear-gradient(135deg,#d9dde2 0%,#8a9098 40%,#3c4148 70%,#e9ecef 100%)}
  .headline{position:absolute;left:574px;font-family:"Oswald",Impact,sans-serif;font-weight:700;line-height:1;
    letter-spacing:-2px;transform-origin:left top;white-space:nowrap}
  .headline-free{top:94px;font-size:177px;color:var(--charcoal);transform:scaleX(0.83)}
  .headline-printer{top:232px;font-size:144px;color:var(--brand-blue);transform:scaleX(0.84)}
  .price-badge{position:absolute;left:926px;top:28px;width:248px;height:248px}
  .price-badge-text{position:absolute;left:926px;top:28px;width:248px;height:248px;display:flex;flex-direction:column;
    align-items:center;justify-content:center;color:var(--white);text-align:center;font-weight:500}
  .price-badge-text .small{font-size:31px;line-height:38px}
  .price-badge-text .amount{font-size:50px;font-weight:700;line-height:54px}
  .tagline{position:absolute;left:576px;top:370px;font-size:37px;line-height:46px;color:var(--ink);white-space:nowrap}
  .plans-band{position:absolute;left:0;top:494px;width:1200px;height:96px;background:var(--brand-blue);
    color:var(--white);font-size:72px;font-weight:500;text-align:center;line-height:96px;text-indent:20px}
  .pricing-note{position:absolute;left:0;top:590px;width:1200px;height:178px;background:var(--pale-band);
    text-align:center;font-size:40px;line-height:48px;padding-top:12px;color:var(--ink);white-space:nowrap}
  .plan{position:absolute;left:0;width:1200px}
  .plan-number{position:absolute;width:104px;height:104px;border-radius:50%;background:var(--brand-blue);
    color:var(--white);font-size:60px;font-weight:500;display:flex;align-items:center;justify-content:center}
  .plan-name{position:absolute;font-size:35px;color:var(--title-blue);white-space:nowrap}
  .plan-desc{position:absolute;font-size:35px;color:#111;white-space:nowrap}
  .plan-perks{position:absolute;list-style:none;font-size:35px;line-height:42px;color:#111;white-space:nowrap}
  .plan-perks li::before{content:"•";font-size:26px;margin-right:8px;vertical-align:3px}
  .plan-perks .wrap{padding-left:26px;display:block}
  .footer{position:absolute;left:0;top:2148px;width:1200px;height:252px;background:var(--footer-grey)}
  .cta-shadow{position:absolute;left:140px;top:2262px;width:920px;height:40px;border-radius:50%;
    background:radial-gradient(ellipse at center,rgba(0,0,0,.45) 0%,rgba(0,0,0,0) 70%)}
  .cta{position:absolute;left:94px;top:2186px;width:1016px;height:94px;border-radius:47px;
    background:linear-gradient(180deg,#1f5a72 0%,#0e3a4e 45%,#06202e 100%);
    color:var(--white);font-family:"Roboto Condensed","Arial Narrow",sans-serif;font-size:54px;
    text-align:center;line-height:94px;letter-spacing:1px}
</style>
</head>
<body>
<main class="banner">
  <section class="hero">
    <div class="hero-photo" role="img" aria-label="Photo of a hand pressing the control panel of an office laser printer"></div>
    <div class="headline headline-free">FREE</div>
    <div class="headline headline-printer">PRINTER</div>
    <svg class="price-badge" viewBox="0 0 248 248" aria-hidden="true">
      <polygon fill="#0c1a44" points="124,0 137,26 154,4 161,33 182,15 182,45 207,34 200,63 228,58 215,85 244,87 225,109 248,124 225,139 244,161 215,163 228,190 200,185 207,214 182,203 182,233 161,215 154,244 137,222 124,248 111,222 94,244 87,215 66,233 66,203 41,214 48,185 20,190 33,163 4,161 23,139 0,124 23,109 4,87 33,85 20,58 48,63 41,34 66,45 66,15 87,33 94,4 111,26"/>
    </svg>
    <div class="price-badge-text">
      <span class="small">Plans</span>
      <span class="small">as low as</span>
      <span class="amount">$9.95/</span>
      <span class="small">month</span>
    </div>
    <p class="tagline">For a monthly cost you get all<br>the supplies and service included</p>
  </section>

  <h2 class="plans-band">5 PLANS AVAILABLE</h2>
  <p class="pricing-note">Prices vary upon printers, most expensive plan is<br>$69.94 a month for a 1 year term and the most affordable<br>plan is $9.95 a month for 3 year term</p>

  <div class="plan" style="top:800px">
    <div class="plan-number" style="left:74px;top:0">1</div>
    <div class="plan-name" style="left:213px;top:8px">MONOCHROME LASER</div>
    <div class="plan-desc" style="left:213px;top:50px">(print only printer, black and white printing)</div>
  </div>

  <div class="plan" style="top:930px">
    <div class="plan-number" style="left:74px;top:0">2</div>
    <div class="plan-name" style="left:213px;top:8px">MULTIFUNCTION MONOCHROME LASER</div>
    <div class="plan-desc" style="left:213px;top:50px">(print scan copy fax printer, black and white printing)</div>
    <ul class="plan-perks" style="left:213px;top:130px">
      <li>Monochrome Printers are given 1000 prints per month</li>
      <li>Toner included</li>
      <li>Service included</li>
      <li>Printer included</li>
    </ul>
  </div>

  <div class="plan" style="top:1254px">
    <div class="plan-number" style="left:76px;top:0">3</div>
    <div class="plan-name" style="left:213px;top:16px">COLOR LASER</div>
    <div class="plan-desc" style="left:213px;top:58px">(print only printer, color printing)</div>
  </div>

  <div class="plan" style="top:1403px">
    <div class="plan-number" style="left:76px;top:0">4</div>
    <div class="plan-name" style="left:213px;top:14px">MULTIFUNCTION COLOR LASER</div>
    <div class="plan-desc" style="left:213px;top:56px">(print scan copy fax, color printing)</div>
    <ul class="plan-perks" style="left:213px;top:136px">
      <li>Color printers are given 500 monochrome prints and 500<span class="wrap">color prints per month</span></li>
      <li>Toner included</li>
      <li>Service included</li>
      <li>Printer included</li>
    </ul>
  </div>

  <div class="plan" style="top:1780px">
    <div class="plan-number" style="left:90px;top:0">5</div>
    <div class="plan-name" style="left:226px;top:14px">INKJET COLOR PRINTER</div>
    <div class="plan-desc" style="left:226px;top:56px">(print copy scan fax, color printing)</div>
    <ul class="plan-perks" style="left:226px;top:136px">
      <li>Inkjet Printers are given 1000 prints per month.</li>
      <li>Ink included</li>
      <li>Service included</li>
      <li>Printer included</li>
    </ul>
  </div>

  <footer class="footer"></footer>
  <div class="cta-shadow" aria-hidden="true"></div>
  <div class="cta">SUBSCRIPTION SERVICE FOR PRINTING</div>
</main>
</body>
</html>
```